Need a corporate background Image with our existing logo for Zoom or Microsoft Teams

Hi,

We require a corporate background image with our existing logo use with Zoom or Microsoft Teams.

Our existing logo is at https://www.halvenrock-systems.com/images/logo_top.png

Thank you.

```html
<!DOCTYPE html>
<html lang="en">
<head>
<meta charset="utf-8">
<title>Halvenrock Systems – Meeting Background</title>
<link href="https://fonts.googleapis.com/css2?family=Archivo:wght@700&display=swap" rel="stylesheet">
<style>
  :root {
    --stage: #9a9a9a;
    --navy-deep: #020633;
    --navy-mid: #061f6e;
    --blue-core: #0d3fa0;
    --brand-blue: #1b7fd4;
    --hex-light: #3aa6ff;
    --hex-mid: #1a63d8;
  }
  * { margin: 0; padding: 0; box-sizing: border-box; }
  html, body {
    width: 1200px;
    height: 899px;
    overflow: hidden;
    background: var(--stage);
  }
  .backdrop {
    position: absolute;
    left: 0;
    top: 112px;
    width: 1200px;
    height: 675px;
    overflow: hidden;
    background:
      radial-gradient(ellipse 45% 32% at 54% 49%, rgba(22, 90, 200, 0.55), transparent 75%),
      linear-gradient(170deg, var(--navy-mid) 0%, var(--blue-core) 40%, var(--navy-mid) 70%, var(--navy-deep) 100%);
  }
  .backdrop::after {
    content: "";
    position: absolute;
    inset: 0;
    background: linear-gradient(105deg, transparent 55%, rgba(2, 6, 51, 0.65) 100%);
    pointer-events: none;
  }
  .hex-sphere {
    position: absolute;
    left: 0;
    top: 0;
    width: 420px;
    height: 675px;
    z-index: 1;
  }
  .brand {
    position: absolute;
    right: 58px;
    top: 40px;
    display: flex;
    align-items: center;
    gap: 16px;
    z-index: 2;
  }
  .brand-dot {
    width: 54px;
    height: 54px;
    border-radius: 50%;
    background: var(--brand-blue);
  }
  .brand-name {
    font-family: "Archivo", Arial, sans-serif;
    font-weight: 700;
    color: var(--brand-blue);
    line-height: 1;
  }
  .brand-name .primary {
    display: block;
    font-size: 42px;
    letter-spacing: -1px;
  }
  .brand-name .secondary {
    display: block;
    margin-top: 8px;
    font-size: 13px;
    text-align: justify;
    text-align-last: justify;
  }
</style>
</head>
<body>
  <main class="backdrop">
    <svg class="hex-sphere" viewBox="0 0 420 675" role="img" aria-label="Glowing blue hexagon mesh sphere emerging from the left edge">
      <defs>
        <radialGradient id="sphereFill" cx="0.45" cy="0.5" r="0.6">
          <stop offset="0" stop-color="var(--hex-mid)" stop-opacity="0.75"/>
          <stop offset="0.55" stop-color="var(--hex-mid)" stop-opacity="0.45"/>
          <stop offset="1" stop-color="var(--hex-light)" stop-opacity="0.25"/>
        </radialGradient>
      </defs>
      <path d="M0 0 L170 0 C330 60 410 230 395 400 C382 540 300 640 160 675 L0 675 Z" fill="url(#sphereFill)"/>
      <path d="M170 0 C330 60 410 230 395 400 C382 540 300 640 160 675" fill="none" stroke="var(--hex-light)" stroke-width="2" stroke-opacity="0.8"/>
    </svg>
    <div class="brand">
      <span class="brand-dot"></span>
      <p class="brand-name">
        <span class="primary">HALVENROCK</span>
        <span class="secondary">S Y S T E M S</span>
      </p>
    </div>
  </main>
</body>
</html>
```